Bold Sparrow Studio
Business Cards, Stationary, T-Shirts
Bold Sparrow Studio -
Creative Brief
Use specific fonts
Feel free to use clear fonts
Bright & Fun-filled
Arch. Dave Tuazon
Business Development Manager
Level C, QRT Business Center 482 Willowgate Street Mandaluyong, Metro Manila
tuazon.ella@brightnestinteriors.com
Okay to use single colors in the background with a different color per sheet. Please make format easily editable to change the names and designations of the people on the business cards
Kitchens Closets Storage Solutions

```html
<!DOCTYPE html>
<html lang="en">
<head>
<meta charset="utf-8">
<title>Brightnest Interiors – Business Card</title>
<link href="https://fonts.googleapis.com/css2?family=Arimo:wght@400;700&display=swap" rel="stylesheet">
<style>
  :root {
    --page-bg: #e9e6e1;
    --card-bg: #ffffff;
    --brand-blue: #1b5fae;
    --brand-blue-dark: #114a8e;
    --brand-green: #7cc243;
    --text-dark: #2b2b2b;
    --text-body: #444444;
  }
  * { margin: 0; padding: 0; box-sizing: border-box; }
  html, body {
    width: 1200px; height: 965px; overflow: hidden;
    background: var(--page-bg);
    font-family: "Arimo", Arial, sans-serif;
  }
  .business-card {
    position: absolute; left: 110px; top: 202px;
    width: 980px; height: 560px;
    background: var(--card-bg);
    border-radius: 26px;
    overflow: hidden;
    box-shadow: 0 6px 18px rgba(0,0,0,0.18);
  }
  .card-swoosh { position: absolute; inset: 0; width: 100%; height: 100%; }
  .brand-block {
    position: absolute; left: 90px; top: 160px; width: 300px;
    text-align: center; color: var(--brand-blue);
  }
  .brand-mark {
    width: 104px; height: 104px; margin: 0 auto 26px;
    background: var(--brand-blue); border-radius: 10px;
  }
  .brand-name { font-weight: 700; font-size: 44px; letter-spacing: 1px; line-height: 1; }
  .brand-sub { font-weight: 700; font-size: 20px; letter-spacing: 1px; margin-top: 6px; }
  .contact-block { position: absolute; left: 447px; top: 162px; color: var(--text-body); }
  .person-name { font-weight: 700; font-size: 40px; color: var(--brand-blue); line-height: 1.1; }
  .person-role { font-size: 22px; color: var(--text-dark); margin-top: 4px; }
  .address { font-size: 21px; line-height: 33px; margin-top: 26px; }
  .contact-list { list-style: none; margin-top: 22px; font-size: 21px; }
  .contact-list li { display: flex; align-items: center; height: 40px; }
  .contact-icon { width: 20px; height: 20px; margin-right: 12px; fill: var(--brand-blue-dark); }
</style>
</head>
<body>
  <div class="business-card">
    <svg class="card-swoosh" viewBox="0 0 980 560" preserveAspectRatio="none" aria-hidden="true">
      <defs>
        <linearGradient id="blueBand" x1="0" y1="0" x2="1" y2="1">
          <stop offset="0" stop-color="#2a7fd0"/>
          <stop offset="1" stop-color="#0f4c96"/>
        </linearGradient>
      </defs>
      <!-- top-right band -->
      <path d="M740 0 C 860 20, 940 120, 980 300 L980 0 Z" fill="#7cc243"/>
      <path d="M775 0 C 880 25, 950 120, 980 270 L980 0 Z" fill="#ffffff"/>
      <path d="M790 0 C 890 30, 955 120, 980 250 L980 0 Z" fill="url(#blueBand)"/>
      <!-- bottom-left band -->
      <path d="M0 300 C 40 430, 120 520, 245 560 L0 560 Z" fill="#7cc243"/>
      <path d="M0 330 C 45 445, 120 525, 215 560 L0 560 Z" fill="#ffffff"/>
      <path d="M0 345 C 45 455, 115 530, 200 560 L0 560 Z" fill="url(#blueBand)"/>
    </svg>

    <div class="brand-block">
      <div class="brand-mark"></div>
      <div class="brand-name">BRIGHTNEST</div>
      <div class="brand-sub">INTERIORS, INC</div>
    </div>

    <div class="contact-block">
      <div class="person-name">Arch. Dave Tuazon</div>
      <div class="person-role">Business Development Manager</div>
      <div class="address">
        Level C, QRT Business Center<br>
        482 Willowgate Street<br>
        Mandaluyong, Metro Manila
      </div>
      <ul class="contact-list">
        <li>
          <svg class="contact-icon" viewBox="0 0 24 24"><path d="M6.6 10.8c1.4 2.8 3.8 5.1 6.6 6.6l2.2-2.2c.3-.3.7-.4 1-.2 1.1.4 2.3.6 3.6.6.6 0 1 .4 1 1V20c0 .6-.4 1-1 1C10.6 21 3 13.4 3 4c0-.6.4-1 1-1h3.5c.6 0 1 .4 1 1 0 1.3.2 2.5.6 3.6.1.3 0 .7-.2 1z"/></svg>
          (632) 718-2046
        </li>
        <li>
          <svg class="contact-icon" viewBox="0 0 24 24"><path d="M7 3h10v5H7zM4 9h16a1 1 0 0 1 1 1v7h-4v4H7v-4H3v-7a1 1 0 0 1 1-1zm5 7v3h6v-3z"/></svg>
          (632) 718-2048
        </li>
        <li>
          <svg class="contact-icon" viewBox="0 0 24 24"><path d="M12 2a10 10 0 1 0 5 18.7l-1-1.7A8 8 0 1 1 20 12v1.2a1.8 1.8 0 0 1-3.6 0V7.5h-2v.9A5 5 0 1 0 15 16a3.8 3.8 0 0 0 7-2.8V12A10 10 0 0 0 12 2zm0 13a3 3 0 1 1 0-6 3 3 0 0 1 0 6z"/></svg>
          tuazon.ella@brightnestinteriors.com
        </li>
      </ul>
    </div>
  </div>
</body>
</html>
```